Larkfield Health Marketing Flyer

We are a new medical practice in the community and need a flyer to send to other medical offices to inform of our services. We just completed our logo with PixelGuild and would like to incorporate that plus our marketing content into the flyer. Our medical practice has 2 divisions: (1)Mental Health/Psychiatry and (2) Migraine and Neurospasticity Management. Please see website for content and provider photos at www.WellLarkvale.com

Target Market(s)

Other Healthcare Professionals in the Community

Industry/Entity Type

Medical

Requirements
Must have
• Photos of all 5 healthcare providers, phone number, address, logo

```html
<!DOCTYPE html>
<html lang="en">
<head>
<meta charset="utf-8">
<title>Larkfield Health – Flyer</title>
<link href="https://fonts.googleapis.com/css2?family=Libre+Baskerville:wght@400;700&family=Arimo:wght@400;700&family=Archivo:wght@900&display=swap" rel="stylesheet">
<style>
  :root{
    --teal:#0f9a88;
    --teal-dark:#0b8677;
    --lime:#a8e05a;
    --green-text:#2fb67a;
    --white:#ffffff;
    --stage:#e3e5e3;
  }
  *{margin:0;padding:0;box-sizing:border-box}
  html,body{width:1200px;height:1200px;overflow:hidden;background:var(--stage)}
  .flyer{position:absolute;left:178px;top:0;width:843px;height:1200px;background:var(--white);overflow:hidden;font-family:"Arimo",Arial,sans-serif}

  .moved{position:absolute;left:21px;top:45px;font-family:"Libre Baskerville",Georgia,serif;font-weight:700;font-size:30px;color:var(--teal-dark);letter-spacing:-0.5px}
  .moved-address{position:absolute;left:24px;top:88px;font-size:15px;font-weight:700;line-height:20px;color:var(--green-text)}

  .brand{position:absolute;left:618px;top:22px;width:194px;text-align:center;font-family:"Libre Baskerville",Georgia,serif;color:var(--teal)}
  .brand-dot{width:52px;height:52px;border-radius:50%;background:var(--teal);margin:0 auto 8px}
  .brand-name{font-size:21px;line-height:25px;letter-spacing:1px}

  .band{position:absolute;left:0;width:843px;background:var(--teal)}
  .band-top{top:138px;height:13px}
  .band-bottom{top:483px;height:12px}

  .hero{position:absolute;left:0;top:151px;width:843px;height:332px;background:linear-gradient(180deg,#32b8aa 0%,#4cc4a2 55%,#86d86a 100%)}
  .hero-photo{position:absolute;right:0;top:0;width:400px;height:332px;background:linear-gradient(160deg,#2fb0a0 0%,#4fbf8e 55%,#8fd55a 100%)}
  .hero-title{position:absolute;left:35px;top:35px;font-family:"Libre Baskerville",Georgia,serif;font-weight:400;font-size:42px;line-height:52px;color:var(--white)}
  .hero-services{position:absolute;left:38px;top:212px;font-size:15px;font-weight:700;line-height:20px;color:var(--white)}

  .providers{position:absolute;left:35px;top:518px;width:770px;display:flex;justify-content:space-between}
  .card{width:142px;display:flex;flex-direction:column}
  .card-photo{display:block;width:142px;height:164px}
  .card-name{height:35px;background:var(--lime);color:var(--teal-dark);font-size:8.2px;font-weight:700;display:flex;align-items:center;justify-content:center;text-align:center;letter-spacing:0.2px}
  .card-bio{height:168px;background:var(--teal);color:var(--white);font-size:7px;font-weight:700;line-height:10.6px;text-transform:uppercase;text-align:center;padding:8px 5px 0}

  .pill{position:absolute;top:903px;height:35px;border-radius:12px;background:var(--lime);box-shadow:2px 3px 0 rgba(0,0,0,0.18);font-family:"Libre Baskerville",Georgia,serif;font-weight:400;font-size:16px;color:var(--teal-dark);display:flex;align-items:center;justify-content:center}
  .pill-left{left:29px;width:312px}
  .pill-right{left:431px;width:378px}
  .section-text{position:absolute;font-size:12.4px;line-height:14.2px;color:var(--green-text)}
  .section-left{left:35px;top:943px;width:330px}
  .section-right{left:470px;top:945px;width:335px;text-align:right}

  .tagline{position:absolute;left:0;top:1064px;width:843px;text-align:center;font-family:"Archivo","Arial Black",sans-serif;font-weight:900;font-size:23px;letter-spacing:1px;color:var(--teal-dark)}

  .footer{position:absolute;left:0;top:1117px;width:843px;height:83px;background:linear-gradient(180deg,#0f9a8c 0%,#15a394 55%,#7fd670 100%);color:var(--white);font-weight:700;font-size:14.5px}
  .contact-row{position:absolute;top:24px;left:0;width:843px;display:flex;justify-content:center;gap:68px}
  .contact-address{position:absolute;top:52px;left:0;width:843px;display:flex;justify-content:center}
  .contact{display:flex;align-items:center;gap:5px}
  .contact svg{display:block}
</style>
</head>
<body>
<main class="flyer">
  <h1 class="moved">WE MOVED!</h1>
  <p class="moved-address">Find us now at 212 Alder Crest Drive, Suite B<br>Larkvale, ID</p>

  <div class="brand">
    <div class="brand-dot"></div>
    <div class="brand-name">LARKFIELD<br>HEALTH</div>
  </div>

  <div class="band band-top"></div>
  <section class="hero">
    <div class="hero-photo" role="img" aria-label="Photo of a smiling woman reading her phone in a bright living room"></div>
    <h2 class="hero-title">Helping Bodies<br>Helping Minds<br>Helping You</h2>
    <p class="hero-services">Mental Health and Psychiatry Services<br>Migraine and Neurospasticity Intervention</p>
  </section>
  <div class="band band-bottom"></div>

  <section class="providers">
    <article class="card">
      <svg class="card-photo" viewBox="0 0 142 164" role="img" aria-label="Portrait of provider Marc Dorland"><polygon points="0,64 142,0 142,164 0,164" fill="#0f9a88"/><rect x="22" y="8" width="100" height="156" rx="40" fill="#c9d6d3"/></svg>
      <div class="card-name">MARC DORLAND, PMHNP - BC</div>
      <p class="card-bio">Before entering into healthcare, Marcus spent years in academia researching foundational cellular and molecular biology mechanisms along with genetics that has provided a strong basis for understanding complex psychiatric conditions and the medications used in behavioral health. Marc cares for teenagers thru adult patient populations.</p>
    </article>
    <article class="card">
      <svg class="card-photo" viewBox="0 0 142 164" role="img" aria-label="Portrait of provider Tessa Caldwell"><polygon points="0,64 142,0 142,164 0,164" fill="#0f9a88"/><rect x="22" y="2" width="100" height="162" rx="40" fill="#c9d6d3"/></svg>
      <div class="card-name">TESSA CALDWELL, PMHNP - BC</div>
      <p class="card-bio">With a former career in the inpatient behavioral health environment, Tessa is excited to share her experience and passion for mental health in an outpatient setting. Her practice cares for teenagers to adults in all aspects of psychiatry and mental wellness.</p>
    </article>
    <article class="card">
      <svg class="card-photo" viewBox="0 0 142 164" role="img" aria-label="Portrait of provider Glen Harrow"><polygon points="0,64 142,0 142,164 0,164" fill="#0f9a88"/><rect x="18" y="0" width="106" height="164" rx="40" fill="#c9d6d3"/></svg>
      <div class="card-name">GLEN HARROW PMHNP - BC</div>
      <p class="card-bio">Formally from North Idaho and having moved back to this area, Glen brings several years of pediatric and adolescent experience to Larkfield Health. Outside of work, Glen enjoys spending time with his wife and two children, exploring various outdoor pursuits including backpacking, fishing, and all things bigfoot.</p>
    </article>
    <article class="card">
      <svg class="card-photo" viewBox="0 0 142 164" role="img" aria-label="Portrait of provider Edith Ransome"><polygon points="0,64 142,0 142,164 0,164" fill="#0f9a88"/><rect x="22" y="0" width="100" height="164" rx="40" fill="#c9d6d3"/></svg>
      <div class="card-name">EDITH RANSOME,PMHNP-BC</div>
      <p class="card-bio">Dr. Edith Ransome is board certified in geriatric and adult psychiatric medicine. She has practiced psychiatry for over 30 years and has extensive experience in the diagnosis and treatment of major mental illnesses. Her passion for mental wellness values the long term relationship with the adult and geriatric patient.</p>
    </article>
    <article class="card">
      <svg class="card-photo" viewBox="0 0 142 164" role="img" aria-label="Portrait of provider Dr. Paul Whitcombe"><polygon points="0,64 142,0 142,164 0,164" fill="#0f9a88"/><rect x="0" y="6" width="142" height="158" rx="40" fill="#d8d2c4"/></svg>
      <div class="card-name">DR. PAUL WHITCOMBE</div>
      <p class="card-bio">A board certified family practice physician, Dr. Paul Whitcombe has incorporated botulinum toxin injections into his practice for several years. Now retired from family medicine, he is devoted to helping patients find relief from migraines and muscle spasticity issues.</p>
    </article>
  </section>

  <h3 class="pill pill-left">Meet Our Mental Health Providers</h3>
  <p class="section-text section-left">Bringing comprehensive evaluation, medication management and psychotherapy to the full spectrum of mental health disorders including minor, moderate and major depression, bipolar disorder, ADD/ADHD, anxiety, schizophrenia, stress or grief reactions, and others.</p>

  <h3 class="pill pill-right">Migraine and Neurospasticity Intervention</h3>
  <p class="section-text section-right">Injections of botulinum neurotoxin are a widely used therapeutic form of treatment for both chronic migraines and patients with involuntary muscle contractions (neurospasticity). Injections may offer up to 3 months of relief and may be combined with other pharmaceutical interventions for maximum benefit.</p>

  <p class="tagline">BOARD CERTIFIED. RESPONSIVE. COMPASSIONATE.</p>

  <footer class="footer">
    <div class="contact-row">
      <span class="contact">
        <svg width="13" height="14" viewBox="0 0 13 14"><rect x="0.5" y="0.5" width="12" height="13" rx="2" fill="#fff"/><path d="M4 3.5c-1 1-.6 3.6 1.6 5.6 2 1.9 3.9 2.2 4.4 1.4l-1.3-1.5-1.2.6c-.9-.5-1.8-1.5-2.2-2.3l.7-1.1L4.8 3z" fill="#0f9a88"/></svg>
        PHONE : 208-555-0147
      </span>
      <span class="contact">
        <svg width="19" height="13" viewBox="0 0 19 13"><rect x="0.7" y="0.7" width="17.6" height="11.6" fill="none" stroke="#fff" stroke-width="1.3"/><path d="M1 1l8.5 6.5L18 1" fill="none" stroke="#fff" stroke-width="1.3"/></svg>
        EMAIL : SUPPORT@WELLLARKVALE.COM
      </span>
    </div>
    <div class="contact-address">
      <span class="contact">
        <svg width="14" height="15" viewBox="0 0 14 15"><path d="M7 1a4 4 0 0 0-4 4c0 3 4 7 4 7s4-4 4-7a4 4 0 0 0-4-4z" fill="none" stroke="#fff" stroke-width="1.3"/><circle cx="7" cy="5" r="1.4" fill="#fff"/><path d="M1 14h12" stroke="#fff" stroke-width="1.3"/></svg>
        ADDRESS : 212 W. ALDER CREST DR, SUITE B LARKVALE, ID&nbsp; 83000
      </span>
    </div>
  </footer>
</main>
</body>
</html>
```